Microlight Aircraft Website Project

Need a website designed, or at least a template made, that my web programmer can work with here. We are a new manufacturer of microlight aircraft & powered hang gliders. Our company name is Brisk Fern. We manufacture portable utility aircraft in the Light Sport category (formerly known as Ultralights or Microlights). Our particular design is a 2-seat powered hang glider and caters to those who want to go explore the backcountry. We are not necessarily aviation nuts, but more into the development of a flying utility vehicle for extreme exploration and expeditions. We have been importing these aircraft from 3 countries for 15 years and have supplied over 200 expedition-quality aircraft world-wide. We are now manufacturing here in the US.

Industry/Entity Type

Manufacturer

Coding

Coded - Design and coding required

```html
<!DOCTYPE html>
<html lang="en">
<head>
<meta charset="utf-8">
<title>Brisk Fern — Powered Hang Gliders</title>
<link href="https://fonts.googleapis.com/css2?family=Roboto:wght@300;400;500&family=Open+Sans:wght@400;600&family=Raleway:wght@400;500&display=swap" rel="stylesheet">
<style>
:root{
  --sky:#29a9e0;
  --navy:#0d4fa0;
  --navy-card:#1a5fa8;
  --ink:#333333;
  --muted:#777777;
  --panel:#f4f4f4;
  --white:#ffffff;
  --star:#f5b301;
  --rule:#bfe3f4;
}
*{box-sizing:border-box;margin:0;padding:0}
html,body{width:696px;height:1200px;overflow:hidden;background:var(--white)}
body{position:relative;font-family:"Open Sans",sans-serif;color:var(--ink)}
.abs{position:absolute}

/* Hero */
.hero{left:0;top:0;width:696px;height:352px;
  background:linear-gradient(172deg,#2f5e9e 0%,#5a86bd 12%,#a7bfd9 22%,#8fb3cf 27%,#3d8fc6 34%,#4f95c4 42%,#6f9a62 50%,#4d7f3a 62%,#7f9a55 72%,#5b7d3c 82%,#3e5a2c 92%,#56703a 100%)}
.hero-brand{left:52px;top:16px;display:flex;align-items:center;gap:6px;font-family:"Roboto",sans-serif;font-weight:500;font-size:14px;color:var(--white);letter-spacing:.3px}
.hero-brand .mark{width:12px;height:12px;border-radius:50%;background:var(--white)}
.account{left:554px;top:19px;font-size:7.5px;color:var(--white)}
.account span{margin:0 4px}
.menu{left:630px;top:21px;width:13px}
.menu i{display:block;height:1.5px;background:var(--white);margin-bottom:2.5px}
.arrow{width:26px;height:26px;border-radius:50%;display:flex;align-items:center;justify-content:center}
.arrow.prev{left:12px;top:164px;background:var(--sky)}
.arrow.next{left:656px;top:164px;background:var(--navy)}

/* About */
.about-back{left:89px;top:386px;width:185px;height:185px;background:linear-gradient(180deg,#1d3f70,#5f7fa6 60%,#7e9ab8)}
.about-front{left:62px;top:412px;width:185px;height:184px;background:linear-gradient(180deg,#5e8fd0 0%,#a9c4e4 62%,#7d8da3 78%,#8a95a4 88%,#d6d9de 100%)}
.about-frame{left:78px;top:430px;width:185px;height:166px;border:2px solid var(--white);border-bottom:none}
.h2{font-family:"Roboto",sans-serif;font-weight:300;font-size:19px;color:var(--sky)}
.h2 b{font-weight:300;color:var(--navy)}
.about-title{left:301px;top:412px}
.bar{height:2px;background:var(--navy)}
.about-bar{left:301px;top:441px;width:22px}
.about-lead{left:300px;top:459px;width:330px;font-family:"Raleway",sans-serif;font-size:10.5px;line-height:16px;color:#222}
.about-body{left:300px;top:497px;width:350px;font-size:7.2px;line-height:13.4px;color:var(--muted)}

/* Products */
.products{left:0;top:624px;width:696px;height:224px;background:var(--panel)}
.section-title{left:0;width:696px;text-align:center}
.products-title{top:641px}
.products-bar{left:330px;top:668px;width:36px}
.card{top:686px;width:140px;height:143px;background:var(--white);border:1px solid #e6e6e6;text-align:center}
.card .shot{margin:2px;width:134px;height:108px}
.shot.green{background:radial-gradient(ellipse 60% 45% at 45% 50%,#4fae4c 0%,#9fd29a 35%,#f6f6f6 70%,#dedede 100%)}
.shot.blue{background:radial-gradient(ellipse 60% 45% at 50% 48%,#2a63c0 0%,#e3d44a 28%,#9bb7e0 45%,#f6f6f6 72%,#dedede 100%)}
.shot.dark{background:radial-gradient(ellipse 55% 50% at 55% 45%,#4a4e55 0%,#8a8f96 35%,#f4f4f4 72%,#dedede 100%)}
.card .name{font-family:"Roboto",sans-serif;font-size:8.5px;color:#222;margin-top:4px}
.stars{font-size:7px;letter-spacing:.5px;color:var(--star)}
.stars .off{color:#bbb}
.card.active{background:var(--navy-card);border-color:var(--navy-card);color:var(--white)}
.card.active .name{color:var(--white);font-size:10.5px;margin-top:30px}
.card.active p{font-size:6.8px;line-height:11.5px;padding:3px 10px 5px}
.card.active .stars .off{color:var(--white)}
.tools{display:flex;justify-content:center;gap:3px;margin-top:6px}
.tools span{width:22px;height:22px;border-radius:50%;display:flex;align-items:center;justify-content:center}
.tools .zoom{background:var(--sky)}
.tools .link{background:var(--white)}

/* Testimonials */
.testimonial-title{top:862px}
.testimonial-bar{left:328px;top:889px;width:38px}
.quote-block .tile{width:87px;height:86px;background:var(--navy)}
.quote-block .photo{width:86px;height:88px}
.quote-block .frame{width:89px;height:86px;border:2px solid var(--sky)}
.quote-name{font-family:"Roboto",sans-serif;font-size:8.5px;color:var(--sky)}
.quote-name em{font-style:normal;font-family:Georgia,serif;font-size:20px;color:#e2e2e2;vertical-align:-6px;margin-right:3px}
.quote-text{width:172px;font-size:6.8px;line-height:12.8px;color:var(--muted)}
.dots i{display:block;width:5px;height:5px;border-radius:50%;background:#dcdcdc;margin-bottom:2px}
.dots i.on{background:var(--sky)}

/* Footer */
.footer{left:0;top:1034px;width:696px;height:143px;background:var(--panel)}
.foot-brand{left:42px;top:1052px;display:flex;align-items:center;gap:6px;font-family:"Roboto",sans-serif;font-weight:500;font-size:15px;color:var(--navy)}
.foot-brand .mark{width:13px;height:13px;border-radius:50%;background:var(--sky)}
.foot-about{left:50px;top:1079px;width:140px;font-size:6.8px;line-height:12.8px;color:#555}
.social{left:50px;top:1126px;display:flex;gap:5px}
.social i{width:15px;height:15px;border-radius:50%;background:var(--navy)}
.social i:first-child{background:var(--sky)}
.foot-head{top:1049px;font-family:"Roboto",sans-serif;font-weight:400;font-size:12.5px;color:var(--sky)}
.foot-list{top:1071px;list-style:none;font-size:6.6px;color:#444}
.foot-list li{height:14px;line-height:10px;padding-left:12px;position:relative}
.foot-list li::before{content:"";position:absolute;left:0;top:3px;width:4px;height:4px;border-radius:50%;background:var(--sky)}
.contact-row{left:502px;width:126px;display:flex;gap:10px;font-size:6.6px;line-height:11.5px;color:#444}
.contact-row svg{flex:none;margin-top:2px}
.contact-rule{left:502px;width:126px;height:1px;background:var(--rule)}
.copyright{left:0;top:1177px;width:696px;height:23px;background:var(--navy);color:var(--white);font-size:6.6px;text-align:center;line-height:23px}
</style>
</head>
<body>

<section class="hero abs" role="img" aria-label="Photo of a pilot launching a white hang glider from a mountain ramp above lakes and farmland"></section>
<div class="hero-brand abs"><span class="mark"></span>BRISK FERN</div>
<div class="account abs">Log In<span>|</span>Register</div>
<div class="menu abs"><i></i><i></i><i></i></div>
<div class="arrow prev abs"><svg width="8" height="10" viewBox="0 0 8 10"><path d="M6 1 2 5l4 4" fill="none" stroke="#fff" stroke-width="1.6"/></svg></div>
<div class="arrow next abs"><svg width="8" height="10" viewBox="0 0 8 10"><path d="M2 1l4 4-4 4" fill="none" stroke="#fff" stroke-width="1.6"/></svg></div>

<div class="about-back abs" role="img" aria-label="Photo of a paraglider in a dark blue sky"></div>
<div class="about-front abs" role="img" aria-label="Photo of a hang glider with orange wing flying over hills"></div>
<div class="about-frame abs"></div>
<h2 class="h2 about-title abs">About <b>us</b></h2>
<div class="bar about-bar abs"></div>
<p class="about-lead abs">We have been importing these aircraft from 3 countries for 15 years and have supplied over 200 expedition-quality aircraft world-wide.</p>
<p class="about-body abs">We are a new manufacturer of microlight aircraft &amp; powered hang gliders. Our company name is Brisk Fern. We manufacture portable utility aircraft in the Light Sport category (formerly known as Ultralights or Microlights). Our particular design is a 2-seat powered hang glider and caters to those who want to go explore the backcountry.</p>

<section class="products abs"></section>
<h2 class="h2 section-title products-title abs">Our <b>Products</b></h2>
<div class="bar products-bar abs"></div>
<div class="card abs" style="left:52px"><div class="shot green" role="img" aria-label="Green and white hang glider"></div><div class="name">Product 1</div><div class="stars">★★★★<span class="off">☆</span></div></div>
<div class="card active abs" style="left:201px"><div class="name">Product 2</div><p>Lorem Ipsum is simply dummy text of the printing and typesetting industry. Lorem Ipsum standard dummy</p><div class="stars">★★★★<span class="off">★</span></div>
<div class="tools"><span class="zoom"><svg width="8" height="8" viewBox="0 0 8 8"><circle cx="3.3" cy="3.3" r="2.3" fill="none" stroke="#fff" stroke-width="1.1"/><path d="M5 5l2.4 2.4" stroke="#fff" stroke-width="1.2"/></svg></span><span class="link"><svg width="8" height="8" viewBox="0 0 8 8"><path d="M3 5l2-2M2.3 3.7 1.3 4.7a1.4 1.4 0 0 0 2 2l1-1M5.7 4.3l1-1a1.4 1.4 0 0 0-2-2l-1 1" fill="none" stroke="#1a5fa8" stroke-width="1"/></svg></span></div></div>
<div class="card abs" style="left:352px"><div class="shot blue" role="img" aria-label="Blue and yellow hang glider"></div><div class="name">Product 3</div><div class="stars">★★★★<span class="off">☆</span></div></div>
<div class="card abs" style="left:502px"><div class="shot dark" role="img" aria-label="Two-seat powered hang glider trike with dark wing"></div><div class="name">Product 4</div><div class="stars">★★★★<span class="off">☆</span></div></div>

<h2 class="h2 section-title testimonial-title abs">Client <b>Testimonial</b></h2>
<div class="bar testimonial-bar abs"></div>
<div class="dots abs" style="left:27px;top:941px"><i></i><i class="on"></i><i></i></div>

<div class="quote-block">
  <div class="tile abs" style="left:50px;top:906px"></div>
  <div class="photo abs" style="left:61px;top:916px;background:linear-gradient(160deg,#7a8a70,#5a3e2c 60%,#3b2a20)" role="img" aria-label="Portrait of a client in a brown jacket outdoors"></div>
  <div class="frame abs" style="left:69px;top:924px"></div>
  <div class="quote-name abs" style="left:166px;top:923px"><em>“</em>Dorian Vale</div>
  <p class="quote-text abs" style="left:170px;top:948px">Lorem Ipsum is simply dummy text of the printing and typesetting industry. Lorem Ipsum has been the industry's standard dummy text ever since the 1500s</p>
</div>
<div class="quote-block">
  <div class="tile abs" style="left:356px;top:906px"></div>
  <div class="photo abs" style="left:367px;top:916px;background:linear-gradient(160deg,#c9d3dc,#7a5a48 55%,#2a2e34)" role="img" aria-label="Portrait of a client by the water"></div>
  <div class="frame abs" style="left:375px;top:924px"></div>
  <div class="quote-name abs" style="left:472px;top:923px"><em>“</em>Ravi Holt</div>
  <p class="quote-text abs" style="left:476px;top:948px">Lorem Ipsum is simply dummy text of the printing and typesetting industry. Lorem Ipsum has been the industry's standard dummy text ever since the 1500s</p>
</div>

<footer class="footer abs"></footer>
<div class="foot-brand abs"><span class="mark"></span>BRISK FERN</div>
<p class="foot-about abs">Lorem Ipsum is simply dummy text of the printing and typesetting industry. Lorem Ipsum has been the industry's</p>
<div class="social abs"><i></i><i></i><i></i><i></i></div>

<h3 class="foot-head abs" style="left:213px">Products</h3>
<ul class="foot-list abs" style="left:213px"><li>Product 1</li><li>Product 2</li><li>Product 3</li><li>Product 4</li><li>Product 5</li><li>Product 6</li></ul>

<h3 class="foot-head abs" style="left:350px">Quick Links</h3>
<ul class="foot-list abs" style="left:350px"><li>Home</li><li>About</li><li>Products</li><li>FAQ</li><li>Privacy Policy</li><li>Terms &amp; Condition</li></ul>

<h3 class="foot-head abs" style="left:501px">Contact us</h3>
<div class="contact-row abs" style="top:1073px"><svg width="14" height="12" viewBox="0 0 14 12"><path d="M4 1a3 3 0 0 1 3 3c0 2-3 5-3 5S1 6 1 4a3 3 0 0 1 3-3z" fill="none" stroke="#29a9e0" stroke-width="1.1"/><circle cx="4" cy="4" r="1" fill="#29a9e0"/><path d="M8 10c2-1 4 0 5-2" fill="none" stroke="#29a9e0"/></svg><div>Lindenweg 42b<br>10117 Harrow</div></div>
<div class="contact-rule abs" style="top:1101px"></div>
<div class="contact-row abs" style="top:1106px"><svg width="14" height="12" viewBox="0 0 14 12"><path d="M1 4c0-2 12-2 12 0v1h-3V4H4v1H1z" fill="#29a9e0"/><rect x="3" y="6" width="8" height="5" rx="1" fill="#29a9e0"/></svg><div>+123-555-0148<br>hello@briskfern.test</div></div>
<div class="contact-rule abs" style="top:1134px"></div>
<div class="contact-row abs" style="top:1142px"><svg width="14" height="12" viewBox="0 0 14 14"><circle cx="7" cy="7" r="5.5" fill="none" stroke="#29a9e0" stroke-width="1.3"/><path d="M7 4v3.3h2.5" fill="none" stroke="#29a9e0" stroke-width="1.2"/></svg><div>Monday - Friday<br>9:00 - 17:00</div></div>

<div class="copyright abs">Copyright 2016 . All Right Reserved</div>

</body>
</html>
```